Woman owned consulting company needs an elegant and modern business card design

I need a business card design for my new consulting company, Mara Quill Consulting. I am looking for something that is simple and elegant, but also creative and original. You can use either version of the logo that are attached. I have also included the information that needs to be featured on the business card.

Requirements
Must have
• The logo and the font type and a standard business card size. Use shades of gray/silver and or rose gold that are in the logo.
• I didn't realize that my actual logo wasn't attached. Please incorporate in the designs.
Should not have
• Colors that are different from my logo

```html
<!DOCTYPE html>
<html lang="en">
<head>
<meta charset="UTF-8">
<title>Mara Quill Consulting – Business Card</title>
<link href="https://fonts.googleapis.com/css2?family=Cormorant+Garamond:wght@400;500;700&display=swap" rel="stylesheet">
<style>
  :root {
    --backdrop: #3b3b3c;
    --card: #141415;
    --card-edge: #1e1e20;
    --silver: #d9d9db;
    --silver-soft: #bdbdc0;
    --muted: #8e8e92;
  }
  * { margin: 0; padding: 0; box-sizing: border-box; }
  html, body {
    width: 799px;
    height: 1200px;
    overflow: hidden;
    background: var(--backdrop);
    font-family: "Cormorant Garamond", Georgia, serif;
  }
  .sheet {
    position: relative;
    width: 799px;
    height: 1200px;
  }
  .card {
    position: absolute;
    left: 80px;
    width: 640px;
    height: 366px;
    background: var(--card);
    border: 1px solid var(--card-edge);
    border-radius: 4px;
    box-shadow: 0 18px 40px rgba(0, 0, 0, 0.45);
  }
  .card--front { top: 150px; }
  .card--back { top: 700px; }

  .brand-name {
    color: var(--silver);
    font-weight: 500;
    font-size: 42px;
    letter-spacing: 0.5px;
    white-space: nowrap;
  }
  .card--front .brand-name {
    position: absolute;
    left: 0;
    right: 0;
    top: 150px;
    text-align: center;
  }
  .card--back .brand-name {
    position: absolute;
    left: 48px;
    top: 110px;
    font-size: 30px;
  }

  .contact {
    position: absolute;
    left: 352px;
    top: 176px;
    color: var(--silver);
  }
  .contact__name {
    font-weight: 700;
    font-size: 25px;
    letter-spacing: 1.5px;
    text-transform: uppercase;
  }
  .contact__role {
    font-size: 16px;
    color: var(--silver-soft);
    margin-bottom: 20px;
  }
  .contact__list {
    list-style: none;
    font-size: 16px;
    line-height: 1.45;
    color: var(--silver-soft);
  }
</style>
</head>
<body>
  <main class="sheet">
    <section class="card card--front" aria-label="Business card front">
      <p class="brand-name">Mara Quill Consulting</p>
    </section>

    <section class="card card--back" aria-label="Business card back">
      <p class="brand-name">Mara Quill Consulting</p>
      <div class="contact">
        <h1 class="contact__name">Mara Quill</h1>
        <p class="contact__role">Owner</p>
        <ul class="contact__list">
          <li>C: 610-555-0142</li>
          <li>E: mara@maraquillconsulting.com</li>
          <li>W: www.maraquillconsulting.com</li>
        </ul>
      </div>
    </section>
  </main>
</body>
</html>
```